Menu - Pasted on vinyl outside of food truck

I would like to provide a simple and easy to read the menu. The menu will have a right and left-side. On the left, I will give the clients option "Your way" see attachment and on the right "Marisol's way" see attachment. Separate menus have been written. "Marisol's way" should receive more attention, colorful images could be used. and make a small space for Lunch and breakfast menu, see attachment.

Clients should have an easy way to pick and understand items on the menu. Use existing logo colors

Target Market(s)

Mexican food lovers

Industry/Entity Type

Food Truck

Font styles to use
Sans Serif

Colors
f78f20
f37122
000000
757575

Requirements
Nice to have
• colors used on existing logo see attachment

```html
<!DOCTYPE html>
<html lang="en">
<head>
<meta charset="utf-8">
<title>Doña Marisol Tacos — Truck Menu</title>
<link rel="stylesheet" href="https://fonts.googleapis.com/css2?family=Alfa+Slab+One&family=Montserrat:wght@400;500;600;700;800&display=swap">
<style>
  :root {
    --orange: #f78f20;
    --orange-deep: #f37122;
    --ink: #1a1a1a;
    --grey: #757575;
    --paper: #ffffff;
    --backdrop: #dcd8d3;
  }
  * { box-sizing: border-box; margin: 0; padding: 0; }
  html, body { width: 1200px; height: 1200px; overflow: hidden; background: var(--backdrop); }
  body { position: relative; font-family: "Montserrat", sans-serif; color: var(--ink); }

  .menu {
    position: absolute; left: 0; top: 177px;
    width: 908px; height: 640px;
    background: var(--paper);
    transform: scale(1.3216); transform-origin: 0 0;
    overflow: hidden;
  }
  .frames { position: absolute; inset: 0; width: 908px; height: 640px; }
  .abs { position: absolute; }

  .slab {
    font-family: "Alfa Slab One", serif;
    font-weight: 400;
    font-synthesis: none;
    color: var(--orange-deep);
    white-space: nowrap;
  }

  /* brand */
  .brand { left: 404px; top: 44px; width: 120px; text-align: center; }
  .brand-dot { width: 14px; height: 14px; border-radius: 50%; background: var(--orange-deep); margin: 0 auto 6px; }
  .brand-name { font-weight: 800; font-size: 13px; line-height: 1.15; color: var(--orange-deep); text-transform: uppercase; }

  /* item choice */
  .item-title { left: 26px; top: 91px; padding: 0 11px; background: var(--paper); font-size: 17px; line-height: 16px; }
  .item-title::before, .item-title::after {
    content: ""; position: absolute; top: 12px; border: 4px solid transparent;
  }
  .item-title::before { left: 1px; border-right-color: var(--orange-deep); border-left: 0; }
  .item-title::after { right: 1px; border-left-color: var(--orange-deep); border-right: 0; }

  .item { left: 36px; width: 120px; }
  .item-price { font-weight: 600; font-size: 14px; line-height: 16px; }
  .item-name { font-weight: 700; font-size: 7px; color: var(--orange-deep); text-transform: uppercase; letter-spacing: .3px; margin-top: 2px; }
  .item-name b { color: var(--ink); }
  .item-desc { font-size: 5.6px; line-height: 10px; color: var(--ink); }

  .meat { left: 188px; top: 122px; }
  .meat-title { font-weight: 600; font-size: 10.5px; color: var(--orange-deep); text-transform: uppercase; letter-spacing: .3px; line-height: 11px; }
  .meat-sub { font-size: 5.5px; font-weight: 600; text-transform: uppercase; line-height: 6px; }
  .rule { width: 38px; height: 1px; background: var(--ink); margin: 10px 0 8px; }
  .meat ul { list-style: none; }
  .meat li { font-size: 7.3px; font-weight: 700; text-transform: uppercase; line-height: 13.7px; letter-spacing: .3px; }
  .meat li::before { content: "•"; margin-right: 6px; }

  .toppings { left: 169px; top: 303px; width: 223px; height: 167px; background: var(--orange); padding: 11px 12px 0 20px; }
  .toppings h3 { font-size: 10.5px; font-weight: 600; color: var(--paper); letter-spacing: .8px; text-transform: uppercase; }
  .toppings .rule { background: var(--paper); margin: 9px 0 6px; }
  .topping { display: flex; justify-content: space-between; align-items: baseline; height: 23px; }
  .topping span { font-size: 6.6px; font-weight: 700; letter-spacing: .6px; text-transform: uppercase; }
  .topping strong { font-size: 10px; font-weight: 600; }

  /* breakfast & lunch */
  .breakfast-tag { left: 0; top: 490px; width: 169px; height: 62px; background: var(--orange); padding: 10px 0 0 35px; color: var(--paper); }
  .breakfast-tag .big, .lunch .big { font-size: 15px; font-weight: 600; line-height: 16px; }
  .breakfast-tag .label { font-size: 10px; font-weight: 600; letter-spacing: .4px; line-height: 11px; }
  .breakfast-tag .label-sub { font-size: 5.6px; line-height: 6px; text-transform: uppercase; color: var(--ink); }
  .lunch { right: 515px; top: 500px; text-align: right; color: var(--orange-deep); }
  .lunch .label { font-size: 10px; font-weight: 700; letter-spacing: .8px; line-height: 11px; }
  .lunch .label-sub { font-size: 5.6px; color: var(--ink); text-transform: uppercase; margin-top: 4px; letter-spacing: .2px; }

  .sub-head { font-size: 6px; font-weight: 700; font-variant: small-caps; text-transform: lowercase; letter-spacing: .3px; text-align: center; }
  .opts { display: grid; grid-template-columns: 1fr 1fr; font-size: 5.6px; line-height: 10.8px; margin-top: 11px; }
  .opts .r { text-align: right; }
  .breakfast-opts { left: 36px; top: 566px; width: 134px; }
  .lunch-opts { left: 231px; top: 566px; width: 162px; }
  .lunch-opts .sub-head { text-align: right; }

  /* special */
  .special-title { left: 616px; top: 94px; width: 136px; text-align: center; background: var(--paper); font-size: 15px; line-height: 17px; padding: 0 18px; }
  .special-title::before, .special-title::after { content: ""; position: absolute; top: 8px; width: 13px; height: 2px; background: var(--orange-deep); }
  .special-title::before { left: 2px; }
  .special-title::after { right: 2px; }
  .special-box { left: 506px; top: 122px; width: 360px; text-align: center; }
  .special-price { font-size: 19px; font-weight: 600; line-height: 22px; }
  .special-name { font-size: 11px; font-weight: 500; color: var(--orange-deep); letter-spacing: 1.4px; text-transform: uppercase; line-height: 14px; }
  .special-desc { font-size: 5px; line-height: 8px; }
  .special-desc b { font-variant: small-caps; }

  .house { left: 505px; top: 208px; width: 361px; height: 247px; background: var(--orange); padding: 6px; }
  .house-inner { width: 100%; height: 100%; border: 1.2px solid var(--paper); position: relative; }
  .dish { position: absolute; left: 20px; right: 18px; }
  .dish-name { font-size: 7px; font-weight: 700; color: var(--paper); letter-spacing: .5px; text-transform: uppercase; }
  .dish-desc { font-size: 5.5px; line-height: 10px; width: 270px; margin-top: 1px; }
  .dish-price { position: absolute; right: 0; top: -2px; font-size: 10px; font-weight: 700; }

  .ques-label { left: 594px; top: 474px; width: 206px; height: 29px; background: var(--orange); font-size: 9px; font-weight: 600; letter-spacing: 1.4px; text-align: center; line-height: 29px; }
  .ques { left: 532px; width: 310px; }
  .ques .dish-name { color: var(--ink); }
  .ques .dish-desc { width: 230px; }
</style>
</head>
<body>
<main class="menu">
  <svg class="frames" viewBox="0 0 908 640" aria-hidden="true">
    <g fill="none" stroke="#1a1a1a" stroke-width="1.3">
      <path d="M0 105 H358 L392 139 V470 H0"/>
      <path d="M169 526 H190 V640"/>
      <path d="M506 198 V137 L538 105 H835 L866 137 V198 Z"/>
      <path d="M506 640 V490 H866 V640"/>
    </g>
    <g stroke="#1a1a1a" stroke-width="1.6" stroke-linecap="round">
      <path d="M538 140 L544 130 M544 130 L548 143 M536 132 L552 132"/>
      <path d="M830 140 L824 130 M824 130 L820 143 M816 132 L832 132"/>
    </g>
  </svg>

  <div class="abs brand">
    <div class="brand-dot"></div>
    <div class="brand-name">Doña Marisol<br>Tacos</div>
  </div>

  <h2 class="abs slab item-title">ITEM<br>CHOICE</h2>

  <div class="abs item" style="top:165px"><div class="item-price">$2.50</div><div class="item-name">Taco: <b>corn or flour</b></div><div class="item-desc">served with cilantro and onion</div></div>
  <div class="abs item" style="top:217px"><div class="item-price">$5.00</div><div class="item-name">Quesadilla</div><div class="item-desc">1 meat, salad, sour cream</div></div>
  <div class="abs item" style="top:269px"><div class="item-price">$7.00</div><div class="item-name">Torta</div><div class="item-desc">1 meat, beans, let, tom, pickle jal,<br>avocado, sour cream</div></div>
  <div class="abs item" style="top:331px"><div class="item-price">$8.00</div><div class="item-name">Burrito</div><div class="item-desc">1 meat, Beans, rice, lett, tom, pico,<br>sourcream, avoc, sauce</div></div>
  <div class="abs item" style="top:393px"><div class="item-price">$8.00</div><div class="item-name">Bowl</div><div class="item-desc">1 meat, rice, beans, salad,<br>sourcream, avoc, pico</div></div>

  <section class="abs meat">
    <h3 class="meat-title">Choice of meat</h3>
    <p class="meat-sub">All tacos are served with cilantro<br>and onions, unless told otherwise</p>
    <div class="rule"></div>
    <ul>
      <li>Bistec</li><li>Pastor</li><li>Chorizo</li><li>Carnitas</li><li>Picadillo</li>
      <li>Barbacoa</li><li>Chicharron</li><li>Shredded chicken</li><li>Fajita (beef or chicken)</li>
    </ul>
  </section>

  <section class="abs toppings">
    <h3>Additional toppings</h3>
    <div class="rule"></div>
    <div class="topping"><span>Queso fresco</span><strong>$.25</strong></div>
    <div class="topping"><span>Avocado</span><strong>$.25</strong></div>
    <div class="topping"><span>Side of rice</span><strong>$1.50</strong></div>
    <div class="topping"><span>Side of beans</span><strong>$1.50</strong></div>
    <div class="topping"><span>Jalapeño o serrano toreado</span><strong>$.50</strong></div>
  </section>

  <div class="abs breakfast-tag">
    <div class="big">$1.50</div>
    <div class="label">BREAKFAST TACOS</div>
    <div class="label-sub">Flour or corn tortilla</div>
  </div>
  <div class="abs breakfast-opts">
    <div class="sub-head">Egg + 1 item</div>
    <div class="opts">
      <span>• Beans</span><span class="r">Sausage •</span>
      <span>• Nopalitos</span><span class="r">Bacon Chorizo •</span>
      <span>• Chicharron</span><span class="r">Potatoes •</span>
    </div>
  </div>

  <div class="abs lunch">
    <div class="big">$8.00</div>
    <div class="label">LUNCH</div>
    <div class="label-sub">Plate (1 meat, rice beans, 3 tortillas, salad)</div>
  </div>
  <div class="abs lunch-opts">
    <div class="sub-head">Choice of meats</div>
    <div class="opts">
      <span>• Sausage</span><span class="r">Fajita (beef or chicken) •</span>
      <span>• Bacon Chorizo</span><span class="r">Pastor •</span>
      <span>• Potatoes</span><span class="r">Chicharron •</span>
    </div>
  </div>

  <h2 class="abs slab special-title">SPECIAL</h2>
  <section class="abs special-box">
    <div class="special-price">$7.00</div>
    <div class="special-name">Taquitos Doña Marisol</div>
    <p class="special-desc"><b>5 Mini-Tacos, choice of up to two meats: Bistec (fine chopped steak), Pastor, Carnitas, Barbacoa o Chorizo</b><br>Small corn tortilla served with grilled onions, cilantro and raw onions</p>
  </section>

  <section class="abs house">
    <div class="house-inner">
      <div class="dish" style="top:18px"><div class="dish-name">Matamoros street taco</div><div class="dish-desc">Corn tortilla, bistec (chopped steak), Grilled Onions, queso fresco, avocado, Marisol's sauce, cilantro and onions.</div><div class="dish-price">$3.00</div></div>
      <div class="dish" style="top:69px"><div class="dish-name">San Felipe</div><div class="dish-desc">Inhouse Carnitas served with special made Pico De Gallo traditionally served In San Felipe Torres Mochas, Guanajuato.</div><div class="dish-price">$3.00</div></div>
      <div class="dish" style="top:121px"><div class="dish-name">El Pastor</div><div class="dish-desc" style="width:280px">Inhouse Marinated Pork , served with cilantro, red onions, queso fresco and avocado.</div><div class="dish-price">$3.00</div></div>
      <div class="dish" style="top:162px"><div class="dish-name">El Campechano</div><div class="dish-desc" style="width:290px">Bistec (steak) , Chorizo , GRILLED nopalitos and onions served with cilantro and onions</div><div class="dish-price">$3.00</div></div>
      <div class="dish" style="top:203px"><div class="dish-name">El Tejano</div><div class="dish-desc" style="width:290px">Beef Fajita, smoked sausage, grilled bell pepper, grilled onions and jalapeños</div><div class="dish-price">$3.00</div></div>
    </div>
  </section>

  <div class="abs ques-label">QUESADILLA / GRINGAS</div>
  <div class="abs dish ques" style="top:524px"><div class="dish-name">Gringa</div><div class="dish-desc">Folded flour Tortilla stuffed with Melted Oaxaca, Azadero and Quesadilla cheese topped with Pastor cilantro and onions</div><div class="dish-price">$3.50</div></div>
  <div class="abs dish ques" style="top:576px"><div class="dish-name">Sincronizada</div><div class="dish-desc">Folded flour tortilla, grilled ham stuffed with melted Oaxaca, Azadero and Quesadilla cheese, cilantro and onions</div><div class="dish-price">$3.50</div></div>
</main>
</body>
</html>
```